Business Card

We need a business card for a fundraising/sales and marketing company called Brightwell Giving services. The logo colours are Red Black and white. The final design should communicate professional, reliable yet fun and charity minded
Updates

Sorry for the delay. A decision will be made in the next 48 hours. we are stuck between two designs. Kind Regards, Laura Dunmore

Industry/Entity Type

Marketing

```html
<!DOCTYPE html>
<html lang="en">
<head>
<meta charset="utf-8">
<title>Brightwell Giving services – Business Card</title>
<link rel="stylesheet" href="https://fonts.googleapis.com/css2?family=Lato:ital,wght@0,400;0,700;0,900;1,400&display=swap">
<style>
  :root {
    --stage: #5f5f5f;
    --card-white: #ffffff;
    --brand-red: #da1f26;
    --ink: #1e1e1e;
    --muted: #7a7a7a;
    --contact: #555555;
  }
  * { margin: 0; padding: 0; box-sizing: border-box; }
  html, body {
    width: 1200px;
    height: 900px;
    overflow: hidden;
    background: var(--stage);
    font-family: "Lato", Arial, sans-serif;
  }
  .business-card {
    position: absolute;
    left: 120px;
    top: 170px;
    width: 960px;
    height: 560px;
    border-radius: 34px;
    overflow: hidden;
    background: var(--card-white);
  }
  .card-bands {
    position: absolute;
    inset: 0;
    width: 100%;
    height: 100%;
  }
  .card-bands .band { fill: var(--brand-red); }
  .holder {
    position: absolute;
    left: 64px;
    top: 232px;
  }
  .holder-name {
    font-size: 44px;
    font-weight: 400;
    color: var(--ink);
    letter-spacing: 0.5px;
    line-height: 1;
  }
  .holder-name strong { font-weight: 900; }
  .holder-role {
    margin-top: 8px;
    font-size: 24px;
    font-style: italic;
    color: var(--muted);
    letter-spacing: 1px;
  }
  .contact-list {
    position: absolute;
    left: 64px;
    top: 396px;
    list-style: none;
    font-size: 22px;
    line-height: 1.38;
    color: var(--contact);
  }
  .contact-list .label {
    color: var(--brand-red);
    font-weight: 700;
    margin-right: 6px;
  }
  .brand-name {
    position: absolute;
    left: 590px;
    top: 196px;
    display: flex;
    align-items: center;
    gap: 12px;
    white-space: nowrap;
  }
  .brand-dot {
    width: 22px;
    height: 22px;
    border-radius: 50%;
    background: var(--brand-red);
  }
  .brand-word {
    font-size: 36px;
    font-weight: 900;
    color: var(--brand-red);
    letter-spacing: 0.5px;
    line-height: 1;
  }
</style>
</head>
<body>
  <article class="business-card">
    <svg class="card-bands" viewBox="0 0 960 560" preserveAspectRatio="none" aria-hidden="true">
      <polygon class="band" points="0,0 640,0 0,218"/>
      <polygon class="band" points="330,560 960,246 960,560"/>
    </svg>

    <div class="brand-name">
      <span class="brand-dot"></span>
      <span class="brand-word">BRIGHTWELL</span>
    </div>

    <header class="holder">
      <h1 class="holder-name">ROWAN <strong>ASHBY</strong></h1>
      <p class="holder-role">MANAGING DIRECTOR</p>
    </header>

    <ul class="contact-list">
      <li><span class="label">m.</span>0400 555 217</li>
      <li><span class="label">w.</span>www.brightwellgivingservices.com</li>
      <li><span class="label">e.</span>rowan@brightwellgivingservices.com</li>
    </ul>
  </article>
</body>
</html>
```